real esate business card with company logo and name

we need a business card design for a real esate company

The company name is Walsh & Brody Pty Ltd, and we have our logo designed and will upload. We want classic or moden feel. Black or white background. looks more textured. Should include folowinginformations
Paul Walsh and Lucy Brody
Sales Agents & Onsite Manager
p: 07 5948 2063
F: 07 5948 2174
M:0461 857 239
3/42 Marlin Crescent, ELLEN GROVE QLD 4078

We want this business card looks professonal. Thank you in advance.

Industry/Entity Type

Real Estate Agent

Contact Information for Business Card

Paul Walsh and Lucy Brody
Onsite Manager & Sales Agents
p: 07 5948 2063
M:0461 857 239

Font styles to use
Serif

Colors
000000
fbfbfb
333333
959595

Requirements
Must have
• company logo and name, black or white back ground

```html
<!DOCTYPE html>
<html lang="en">
<head>
<meta charset="utf-8">
<title>Walsh &amp; Brody Pty Ltd — Business Card</title>
<link rel="stylesheet" href="https://fonts.googleapis.com/css2?family=Open+Sans:wght@400;600&family=Oswald:wght@300;400&display=swap">
<style>
  :root {
    --backdrop: #000000;
    --card: #343437;
    --card-edge: #3a3a3d;
    --ink-light: #fbfbfb;
    --ink-mid: #959595;
    --rule: #55555a;
  }
  * { margin: 0; padding: 0; box-sizing: border-box; }
  html, body {
    width: 1200px; height: 900px; overflow: hidden;
    background: var(--backdrop);
  }
  .stage { position: relative; width: 1200px; height: 900px; }
  .card {
    position: absolute; top: 271px;
    width: 457px; height: 281px;
    border-radius: 14px;
    background:
      repeating-linear-gradient(0deg, rgba(255,255,255,0.012) 0 1px, transparent 1px 3px),
      var(--card);
    box-shadow: inset 0 0 0 1px var(--card-edge);
  }
  .card--front { left: 137px; }
  .card--back { left: 626px; }

  .brand-mark {
    position: absolute;
    display: flex; align-items: center; justify-content: center; gap: 10px;
    font-family: "Oswald", "Arial Narrow", sans-serif;
    font-weight: 400; color: var(--ink-mid);
    letter-spacing: 0.02em; white-space: nowrap;
  }
  .brand-mark__square { background: var(--ink-mid); flex: none; }

  .card--front .brand-mark { left: 30px; top: 118px; width: 190px; font-size: 20px; }
  .card--front .brand-mark__square { width: 14px; height: 14px; }

  .divider {
    position: absolute; left: 219px; top: 66px;
    width: 1px; height: 156px; background: var(--rule);
  }
  .details {
    position: absolute; left: 235px; top: 60px;
    font-family: "Open Sans", "Segoe UI", sans-serif;
    color: var(--ink-light);
  }
  .details__names { font-size: 14.5px; font-weight: 600; color: var(--ink-mid); line-height: 20px; }
  .details__role { font-size: 12.5px; line-height: 17px; }
  .details__phones { margin-top: 31px; list-style: none; }
  .details__phones li {
    display: flex; align-items: center; gap: 8px;
    font-size: 12.5px; line-height: 19px;
  }
  .details__phones svg { width: 11px; height: 11px; flex: none; }
  .details__address { margin-top: 18px; font-size: 12.5px; line-height: 19px; font-style: normal; }

  .card--back .brand-mark { left: 0; top: 95px; width: 100%; font-size: 34px; gap: 14px; }
  .card--back .brand-mark__square { width: 22px; height: 22px; }
  .company-name {
    position: absolute; left: 0; top: 215px; width: 100%;
    text-align: center;
    font-family: "Oswald", "Arial Narrow", sans-serif;
    font-weight: 300; font-size: 21px; letter-spacing: 0.03em;
    color: var(--ink-mid);
  }
</style>
</head>
<body>
<main class="stage">
  <section class="card card--front" aria-label="Business card front">
    <div class="brand-mark"><span class="brand-mark__square"></span>Walsh &amp; Brody</div>
    <div class="divider"></div>
    <div class="details">
      <p class="details__names">Paul Walsh and Lucy Brody</p>
      <p class="details__role">Onsite Manager &amp; Sales Agents</p>
      <ul class="details__phones">
        <li>
          <svg viewBox="0 0 12 12" aria-hidden="true"><path fill="#959595" d="M1 4.2C1 2.8 3 2 6 2s5 .8 5 2.2V5H8.6V4H3.4v1H1zM3 6h6l1.5 3.5v1H1.5v-1z"/></svg>
          07 5948 2063
        </li>
        <li>
          <svg viewBox="0 0 12 12" aria-hidden="true"><rect x="3.5" y="0.8" width="5" height="10.4" rx="1" fill="none" stroke="#959595" stroke-width="1"/><rect x="5.3" y="9.2" width="1.4" height="0.8" fill="#959595"/></svg>
          0461 857 239
        </li>
      </ul>
      <address class="details__address">3/42 Marlin Crescent,<br>HARLOW PARK QLD 4519</address>
    </div>
  </section>

  <section class="card card--back" aria-label="Business card back">
    <div class="brand-mark"><span class="brand-mark__square"></span>Walsh &amp; Brody</div>
    <p class="company-name">WALSH &amp; BRODY PTY LTD.</p>
  </section>
</main>
</body>
</html>
```